Halvorsen Partners Business Card

Halvorsen Partners Civil Construction
Marcus Halvorsen
CEO
727-518-6094
Marcus@HalvorsenSiteworks.example
www.HalvorsenSiteworks.example
Site Development
Utility Construction
Excavation
40876 County Lane 19
Land O' Lakes, FL 34638

Target Market(s)

Construction and government

Industry/Entity Type

Business

Contact Information for Business Card

I want an unique design that make a statement

Number of Pages Required

1 page

Font styles to use

Colors

Designer to choose colors to be used in the design.

Requirements
Must have
• unique design, feel free to modify or change the color of my logo.
Nice to have
• extra design features like spot UV, foil accents, color edges, unique paper, or any thing that would make my card pop.
• I like the feel of the image that I attached

```html
<!DOCTYPE html>
<html lang="en">
<head>
<meta charset="utf-8">
<title>Halvorsen Partners Business Card</title>
<link rel="stylesheet" href="https://fonts.googleapis.com/css2?family=Open+Sans:wght@400;600;700&display=swap">
<style>
  :root {
    --royal: #1a2a8c;
    --royal-deep: #16247a;
    --accent-bar: #2f3fb0;
    --paper: #fbfbfa;
    --ink-grey: #8a8a8a;
    --ink-dark: #3d3d3d;
    --foil: #c9cbd2;
    --foil-dim: #7f88c4;
    --stage: #e9e9e7;
  }
  * { box-sizing: border-box; margin: 0; padding: 0; }
  html, body { width: 1200px; height: 1021px; overflow: hidden; }
  body {
    background: var(--stage);
    font-family: "Open Sans", Arial, sans-serif;
    position: relative;
  }
  .card {
    position: absolute;
    left: 220px;
    width: 760px;
    height: 434px;
    box-shadow: 0 6px 18px rgba(0,0,0,.18);
  }
  .card--front { top: 50px; background: var(--paper); border-bottom: 6px solid var(--royal-deep); }
  .card--back { top: 537px; background: var(--royal); }

  /* front */
  .brand {
    position: absolute; right: 56px; top: 48px;
    display: flex; align-items: center; gap: 14px;
    color: var(--royal);
  }
  .brand__square { width: 46px; height: 46px; background: var(--royal); }
  .brand__name { font-weight: 700; font-size: 22px; letter-spacing: .3px; text-transform: uppercase; line-height: 1.1; }
  .brand__sub { font-weight: 700; font-size: 11px; letter-spacing: 3.6px; text-transform: uppercase; }

  .person {
    position: absolute; left: 40px; top: 170px;
    border-left: 12px solid var(--accent-bar);
    padding-left: 12px;
  }
  .person__name { font-size: 28px; color: var(--ink-grey); line-height: 1.1; font-weight: 400; }
  .person__name strong { font-weight: 700; }
  .person__title { font-size: 19px; color: var(--royal); line-height: 1.2; }

  .contact { position: absolute; left: 52px; bottom: 52px; list-style: none; }
  .contact li { display: flex; align-items: center; gap: 16px; font-size: 17px; color: var(--ink-dark); margin-top: 10px; }
  .contact svg { width: 22px; height: 18px; fill: var(--royal); }

  .site-front { position: absolute; right: 56px; top: 224px; font-size: 16px; color: var(--royal); }

  /* back */
  .back-brand {
    position: absolute; left: 120px; top: 138px;
    display: flex; align-items: center; gap: 22px;
  }
  .back-brand__square { width: 80px; height: 80px; border: 3px solid var(--foil); }
  .back-brand__name { font-size: 38px; font-weight: 600; letter-spacing: 1px; text-transform: uppercase; color: var(--foil); line-height: 1.1; }
  .back-brand__sub { font-size: 18px; font-weight: 600; letter-spacing: 9px; text-transform: uppercase; color: var(--foil); }
  .services {
    position: absolute; left: 0; right: 0; top: 268px; text-align: center;
    font-size: 17px; color: var(--foil-dim); letter-spacing: .4px;
  }
  .services span { margin: 0 12px; }
  .site-back { position: absolute; left: 0; right: 0; top: 330px; text-align: center; font-size: 16px; color: #0f1a5c; }
</style>
</head>
<body>
  <section class="card card--front">
    <div class="brand">
      <div class="brand__square"></div>
      <div>
        <div class="brand__name">Halvorsen Partners</div>
        <div class="brand__sub">Civil Construction</div>
      </div>
    </div>
    <div class="person">
      <h1 class="person__name">Marcus <strong>Halvorsen</strong></h1>
      <p class="person__title">CEO</p>
    </div>
    <p class="site-front">www.HalvorsenSiteworks.example</p>
    <ul class="contact">
      <li>
        <svg viewBox="0 0 22 18" aria-hidden="true"><path d="M2 6c0-3 4-4 9-4s9 1 9 4v1h-4V5c-2-.6-8-.6-10 0v2H2zM5 8h12l2 8H3zm6 2a3 3 0 1 0 0 6 3 3 0 0 0 0-6z"/></svg>
        727-518-6094
      </li>
      <li>
        <svg viewBox="0 0 22 18" aria-hidden="true"><path d="M1 3h20v12H1zm2 1.5 8 6 8-6"/><path d="M3 4l8 6 8-6" fill="none" stroke="#fbfbfa" stroke-width="1.5"/></svg>
        Marcus@HalvorsenSiteworks.example
      </li>
    </ul>
  </section>

  <section class="card card--back">
    <div class="back-brand">
      <div class="back-brand__square"></div>
      <div>
        <div class="back-brand__name">Halvorsen Partners</div>
        <div class="back-brand__sub">Civil Construction</div>
      </div>
    </div>
    <p class="services">Site Development<span>|</span>Utility Construction<span>|</span>Excavation</p>
    <p class="site-back">www.HalvorsenSiteworks.example</p>
  </section>
</body>
</html>
```